BANNER FOR ONLINE CABINET COMPANY MAIN PAGE

Need 3 different banners for the main page. We are online platform for ordering cabinets, parts etc. online.
Website: trimfit.ca
A place where the banner will be placed: https://view.snapvault.example/qR7TpWzKmB4eX
Banner size: 1344x399 pixels
****Clients should get the main point that they can order everything online through the website.

Industry/Entity Type

online cabinets and parts ordering

Requirements
Must have
• online ordering icons, iphone, laptop, desktop pc - so clients get an idea that this is web based service to order cabinets

```html
<!DOCTYPE html>
<html lang="en">
<head>
<meta charset="utf-8">
<title>TrimFit – Custom Cabinets Online</title>
<link href="https://fonts.googleapis.com/css2?family=Anton&family=Roboto:wght@300;400;500;700;900&display=swap" rel="stylesheet">
<style>
:root{
  --bar:#2f3336;
  --panel:#393e42;
  --band:#e5e6e7;
  --ink:#111;
  --muted:#555;
  --white:#fff;
  --green:#2bb34a;
  --orange:#f5a400;
  --dot:#d4d4d4;
  --faint:#e3eef5;
  --chat:#2f3a45;
}
*{margin:0;padding:0;box-sizing:border-box}
html,body{width:1200px;height:545px;overflow:hidden;background:var(--white);font-family:"Roboto",Arial,sans-serif}
.page{position:relative;width:1200px;height:545px;overflow:hidden}
.topbar{position:absolute;left:0;top:0;width:1189px;height:31px;background:var(--bar);color:var(--white)}
.topbar .abs{position:absolute;top:0;height:31px;display:flex;align-items:center;white-space:nowrap}
.brand{left:26px;font-weight:700;font-size:13px;gap:5px}
.brand i{display:inline-block;width:6px;height:6px;background:#e53b2c;margin-top:-8px}
.divider{left:98px;top:6px!important;height:19px!important;width:1px;background:var(--white)}
.tagline{left:111px;font-size:8px}
.contact{left:206px;top:7.5px!important;height:16px!important;width:198px;background:#000;font-size:6.6px;padding-left:6px;gap:5px}
.contact svg{flex:none}
.nav{font-size:7.2px;font-weight:500}
.order{left:719px;top:9px!important;height:13px!important;width:62px;background:var(--green);border-radius:7px;justify-content:center;font-weight:700}
.band{position:absolute;left:0;top:31px;width:1189px;height:58px;background:var(--band);text-align:center}
.band h1{font-weight:900;font-size:19px;letter-spacing:.3px;color:var(--ink);margin-top:5px}
.band p{font-weight:300;font-size:13.5px;color:var(--muted);margin-top:5px}
.hero{position:absolute;left:0;top:89px;width:1189px;height:355px;box-shadow:0 2px 4px rgba(0,0,0,.25)}
.hero-panel{position:absolute;left:0;top:0;width:429px;height:355px;background:var(--panel);color:#f2f2f2}
.devices{position:absolute;left:39px;top:39px}
.hero-title{position:absolute;left:38px;top:92px;font-family:"Anton",Impact,sans-serif;font-size:63px;line-height:66px;letter-spacing:.5px;color:#f0f0f0}
.hero-sub{position:absolute;left:39px;top:230px;font-family:"Anton",Impact,sans-serif;font-size:25px;color:#f0f0f0;letter-spacing:.3px}
.hero-list{position:absolute;left:39px;top:262px;list-style:none;font-size:16px;font-weight:400;line-height:22px;color:#ececec}
.hero-list li::before{content:"• ";}
.hero-photo{position:absolute;left:429px;top:0;width:760px;height:355px;background:linear-gradient(100deg,#c7a183 0%,#b8663c 35%,#a7a9a6 62%,#6e6f6c 80%,#a8aeab 100%)}
.dots{position:absolute;left:544px;top:448px;display:flex;gap:8.6px}
.dots span{width:7px;height:7px;background:var(--dot)}
.dots .on{background:var(--orange)}
.steps-title{position:absolute;left:0;width:1189px;top:476px;text-align:center;font-weight:900;font-size:19px;color:var(--ink)}
.step-num{position:absolute;top:522px;font-weight:900;font-size:44px;color:var(--faint);line-height:1}
.chat{position:absolute;left:1025px;top:525px;width:150px;height:20px;background:var(--chat);border-radius:4px 4px 0 0;color:var(--white);font-size:7px;font-weight:500;padding:6px 0 0 8px}
.chat::after{content:"";position:absolute;right:-2px;top:0;width:12px;height:12px;background:var(--green);border-radius:0 8px 0 12px}
.scroll{position:absolute;left:1189px;top:0;width:11px;height:545px;background:#f1f1f1}
.scroll span{position:absolute;left:2px;top:6px;width:7px;height:84px;background:#c1c1c1}
</style>
</head>
<body>
<div class="page">
  <header class="topbar">
    <div class="abs brand">TrimFit<i></i></div>
    <div class="abs divider"></div>
    <div class="abs tagline">Get the size you need!</div>
    <div class="abs contact">
      <svg width="9" height="9" viewBox="0 0 24 24"><path fill="#fff" d="M6.6 10.8a15 15 0 0 0 6.6 6.6l2.2-2.2c.3-.3.7-.4 1-.2 1.1.4 2.3.6 3.6.6.6 0 1 .4 1 1V20c0 .6-.4 1-1 1A17 17 0 0 1 3 4c0-.6.4-1 1-1h3.5c.6 0 1 .4 1 1 0 1.3.2 2.5.6 3.6.1.3 0 .7-.2 1z"/></svg>
      <span>Call us (403) 555 0182</span>
      <svg width="10" height="10" viewBox="0 0 24 24" style="margin-left:6px"><circle cx="12" cy="12" r="9" fill="none" stroke="#fff" stroke-width="2"/><path d="M12 7v5l3 2" stroke="#fff" stroke-width="2" fill="none"/></svg>
      <span>Mon-Fri 8AM - 4.30PM</span>
    </div>
    <div class="abs nav" style="left:692px">CAD</div>
    <div class="abs nav order">ORDER NOW</div>
    <div class="abs nav" style="left:794px">DESIGN &amp; QUOTE</div>
    <div class="abs nav" style="left:867px">SAMPLES</div>
    <div class="abs nav" style="left:914px">ABOUT</div>
    <div class="abs nav" style="left:953px">CONTACT</div>
    <div class="abs nav" style="left:1001px">ARTICLES</div>
    <div class="abs" style="left:1057px"><svg width="10" height="10" viewBox="0 0 24 24"><circle cx="10" cy="10" r="7" fill="none" stroke="#fff" stroke-width="2"/><path d="M15 15l6 6" stroke="#fff" stroke-width="2"/></svg></div>
    <div class="abs" style="left:1096px;font-weight:900;font-size:14px">?</div>
    <div class="abs" style="left:1130px"><svg width="13" height="13" viewBox="0 0 24 24"><circle cx="12" cy="8" r="5" fill="none" stroke="#fff" stroke-width="2"/><path d="M3 22c1-5 5-7 9-7s8 2 9 7z" fill="none" stroke="#fff" stroke-width="2"/></svg></div>
    <div class="abs" style="left:1163px"><svg width="14" height="13" viewBox="0 0 24 22"><path d="M1 2h4l3 12h12l2-8H7" fill="none" stroke="#fff" stroke-width="1.8"/><circle cx="9" cy="19" r="1.8" fill="#fff"/><circle cx="18" cy="19" r="1.8" fill="#fff"/></svg></div>
  </header>

  <section class="band">
    <h1>THE FIRST ONLINE CUSTOM CABINET’S MANUFACTURER</h1>
    <p>Order custom cabinets online with instant price calculator. No hidden fees, top quality warranty.</p>
  </section>

  <section class="hero">
    <div class="hero-panel">
      <svg class="devices" width="150" height="42" viewBox="0 0 150 42" fill="none" stroke="#e8e8e8" stroke-width="2.2">
        <rect x="4" y="2" width="44" height="30" rx="2"/>
        <path d="M0 35h52v2H0z" fill="#e8e8e8"/>
        <path d="M25 13l0 8 2-2 2 3" stroke-width="1.5"/>
        <rect x="68" y="2" width="38" height="26" rx="1"/>
        <path d="M68 23h38M87 28v6M78 36h18"/>
        <rect x="122" y="2" width="24" height="38" rx="4"/>
        <path d="M130 6h8"/>
      </svg>
      <div class="hero-title">EASY QUOTE<br>&amp; ORDER</div>
      <div class="hero-sub">Textured Melamine</div>
      <ul class="hero-list">
        <li>Lots of Colors in Stock &nbsp;• Easy to Clean</li>
        <li>Everything Made Based on Your Size</li>
        <li>Very Durable Material</li>
      </ul>
    </div>
    <div class="hero-photo" role="img" aria-label="Smiling couple in a modern kitchen holding a countertop sample beside a rack of material samples"></div>
  </section>

  <div class="dots"><span></span><span></span><span></span><span></span><span class="on"></span><span></span><span></span></div>

  <h2 class="steps-title">EASY QUOTE &amp; ORDER</h2>
  <div class="step-num" style="left:259px">1</div>
  <div class="step-num" style="left:428px">2</div>
  <div class="step-num" style="left:600px">3</div>
  <div class="step-num" style="left:781px">4</div>

  <div class="chat">Questions? Start chat, we are online!</div>
  <div class="scroll"><span></span></div>
</div>
</body>
</html>
```